Talvoro Web Design

We need a redesign of our current website www.talvoro-example.com

THIS IS A DESIGN STAGE ONLY

We have attached details of the whole project for your understanding only

We do not want to change our Logo but do want to have a more modern and intuitive feel to the site.

The first stage is the design but we are also looking for a coder to take the site to the next level

Talvoro has a current website that has been in operation for the past 6 years the design was based around the Saas self-service model and while functional does not meet Talvoro needs with regard to the new positioning.

We are happy to stay in Fendrix or will look at alternatives

The purpose of the redesign is to align the look and feel of the website to meet our current new brand position and to provide a access point for the delivery of new content from Blogs and white papers as well as a portal for information for our current users for gathering Tips and Tricks and access to additional resources to assist them to provide feedback and get support.

Talvoro is Australia's only PPM (Project and Portfolio Management) software provider that caters to the needs of project managers and C-level executives looking for insights into the alignment of resources to business strategy and investment decisions.

As companies gain maturity in PPM there is a need for innovation and management of change beyond just implementation of tools this is why Talvoro has evolved from being a SaaS to becoming a SwS (Software with Service) provider.

Talvoro is recognized as the tool of choice amongst program and project managers that is able to provide the user with an intuitive reliable interface that is capable of evolving and maturing to meet and exceed client requirements.

We are able to provide people at the coalface with tools that enable them to manage resources, scope, time sheeting, issues, changes and risk with excellent reporting functionality.

For C-level executives we are able to provide Business Intelligence (BI) functionality and reporting by integrating the PPM data with other business management systems such as ERP and CRM to provide a insight beyond pure PPM reporting.

We are able to provide Project Management insights from years of experience working with our clients in developing solutions that are inline with the evolution that comes with change.

Please feel free to email me on nigel.brask@talvoro-example.com if you require any further details. A Site map and a wire frame is available.

Competitor sites include

www.plonverk-example.com
www.surmoza-example.com
www.qarnitel-example.com
www.velubra-example.com
Updates

Hi All 

We are getting some great designs coming in and really appreciate all of your efforts.

Some feedback to you all is that we have a preference for cleaner designs that take into account comprehension ability. So reverse type to us looks good but doesnt always get the cut through.

We have to remember that this is a marketing site first and foremost so what we are looking for is the ability to engage with our audience and get them to start to explore. That is upto us to provide great content and what we want from the design is the ability to be be able to engage with our Audience.

For your consideration please review this info from our marketing plan

There are 3 main communication groups inthe sales process.

Users-        These are the peoplewho will be at the coal face inputting the data and using the product on adaily basis. It is key to provide them with an easy to use and functional toolthat is able to provide them with the information they are looking for easily andintuitively. They have the capacity to say yes and can push the sale decisionup the chain. They equally have the power to say No and stop the sales processin its tracks. They will have a opinion who or what they feel is the best ofbreed and will try to influence the process.

Users are split into two groups.

Group1- They will be diploma if not degree qualifiedwill be a mix of Male and female with majority aged 18 to 35 they are at thecareer development stage of their life cycle normally on an income 45k to 70kper annum. We would position these people very strongly in the “What is in itfor me”.

Group2- PM who has used a variety of tools and systemsover the years they will be pre disposed to one or more systems and has morethan likely been exposed to MSP. Usually in the 30 to 50 year old age rangewith extensive on the job experience.

KeyInfluencers- These are the people who while notactually utilizing the software need to receive information in the form ofreports etc from the system. They normally don’t have the capacity to say yesbut they most certainly can say no. They will have come from a PM or IT roleand have a strong understanding of the PM processes. Influencers will be 30 to50 years of age they are at the family development stage with strong demandsfrom work and family predominantly male but not exclusively. They would bedegree qualified and possibly have completed or looking at additional studies. Therewill be an emphasis on getting the job done right. They are very time poor and hardto communicate with and engage. While being time poor they have an affinitywith and understand the greater good.

DecisionMakers- These are our key decision makers whilethey may not have direct input into the system or processes they are at the endof the day the people who approve the expenditure.

There is a huge demand for this person’stime with a multitude of people from internal employees and management,suppliers, customers, the community and potential suppliers. They are oftentravelling and going from one subject matter to another meeting after meeting.They will be at the stage where children are gaining some independents or leftthe home, career is stabilized and a clear path is formed. They are very directand deal in the facts and figures when it comes to decision making, they arenormally highly educated to the MBA or Doctorate level. They will be driven byoutcomes not the process of getting there.

 

A consistent theme across this group isthe following.

Psychographics

·Values time and considers ittheir single most limited resource.

·Excited about accepting andusing innovative ideas and products always wants to be at the fore front.

·Value adding has priority overprice

·Consistent web users: preferinternet over magazines and newspapers

Behavior

·They are leaders in productselection and respond to the opinions of the ‘Industry Experts’ when makingpurchase decisions.

·This group will look to theinternet to acquire the information

·Will make an informed decisionto purchase after due consideration.

·This group can be a powerfulsales force resulting from the referral network they build and use

Hope this helps

Hi All

Sorry for the delay we are in the final stages of decisions, so sorry we have had people away from the office who need to be involved in the process.

We will submit individual questions to those in the running and let all of the people who didnt get through this time as to why shortly.

We would like to thank you all for your efforts and submissions.

Regards

Nigel Brask 

Industry/Entity Type

Business Management

Requirements
Must have
• The scope of the website is to provide a modern functional website that is easy to navigate and provides a range of products and services to meet the needs of our potential clients and current users.

Two potential groups of viewers exist:
1. Potential Clients and users from the Project management community these would be split into 3 distinct groups. ( Please refer to Page 20 Talvoro marketing Plan)
a. Project Managers
b. Project Directors
c. Business Managers
2. Current Talvoro Users

The goal of website is to engage with the project management community reinforcing the Talvoro Brand as Software with Service the key ethos should be around the company being thought leaders and industry experts with a strong commitment to clients and the success of their Portfolio/Program Management Office

Maintaining a modern and user friendly site is of the highest importance in order to hold users attention and guide the viewer to information that will lead to a decision to pursue accreditation and association with the Talvoro Brand

We would like to guide potential clients to want to engage with us in assisting them to understand their current position in the P3M3 maturity model and to use us as a source for information and guidance.

Benefits for using the site should include:
• Information from a broad spectrum of Project Management professionals and recognized industry experts.
• Information on the Talvoro Product and Services
• Timely and up to date information that encourages readers to return to the site
• Call to action, and plans for potential users of Talvoro software.
• Demonstrate the benefits of accreditation and Call to action for current users to gain accreditation.
• Call to action for attending monthly webinars
• Ability to review past webinars, whitepapers etc.

```html
<!DOCTYPE html>
<html lang="en">
<head>
<meta charset="utf-8">
<title>Talvoro – Project Management Software</title>
<link rel="stylesheet" href="https://fonts.googleapis.com/css2?family=PT+Sans:wght@400;700&family=Roboto+Condensed:wght@400;700&display=swap">
<style>
:root{
  --header:#1f1f1f;
  --subnav:#2e2e2e;
  --nav-active:#4a4a4a;
  --nav-muted:#8c8c8c;
  --hero-dark:#2e3c4a;
  --hero-light:#66788a;
  --accent:#e0401f;
  --orange:#f36c21;
  --text:#444;
  --rule:#dcdcdc;
  --btn:#555;
  --footer:#4b4b4b;
  --footer-bar:#575757;
  --footer-text:#d8d8d8;
  --badge-light:#bdbdbd;
  --badge-dark:#2a2a2a;
}
*{margin:0;padding:0;box-sizing:border-box}
html,body{width:1143px;height:1200px;overflow:hidden;background:#fff}
body{font-family:"PT Sans",sans-serif}
.page{width:1400px;height:1470px;position:relative;transform:scale(.8164);transform-origin:0 0}
.abs{position:absolute}

.header{top:0;left:0;width:1400px;height:115px;background:var(--header)}
.logo{left:210px;top:38px;display:flex;align-items:center;gap:10px}
.logo-dot{width:16px;height:16px;border-radius:50%;background:var(--orange)}
.logo-name{color:#fff;font-size:46px;font-weight:400;line-height:1}
.topnav a{position:absolute;top:0;height:115px;line-height:150px;text-align:center;color:var(--nav-muted);font-weight:700;font-size:13px;text-decoration:none}
.topnav a.active{background:#3b3b3b}

.subnav{top:115px;left:0;width:1400px;height:48px;background:var(--subnav)}
.subnav a{position:absolute;top:0;height:48px;line-height:48px;color:#fff;font-size:12px;text-decoration:none;text-align:center}
.subnav a.active{background:var(--nav-active)}

.hero{top:163px;left:0;width:1400px;height:474px;background:radial-gradient(ellipse 520px 420px at 420px 200px,var(--hero-light),var(--hero-dark) 70%,#2a3744)}
.hero-art{left:220px;top:0;width:550px;height:474px;background:radial-gradient(circle at 200px 170px,#c9d2da,#7d8c99 40%,rgba(60,75,90,0) 75%)}
.hero-copy{left:760px;top:125px;color:#fff;font-family:"Roboto Condensed",sans-serif}
.hero-copy h1{font-size:38px;font-weight:400;line-height:42px;letter-spacing:-.5px}
.hero-copy p{margin-top:14px;font-size:24px;line-height:33px;width:470px;letter-spacing:-.3px}
.hero-btn{left:997px;top:308px;width:193px;height:40px;background:linear-gradient(#e0e0e0,#a9a9a9);border:1px solid #ccc;color:#3a3a3a;font-family:"Roboto Condensed",sans-serif;font-size:18px;line-height:40px;text-align:center}

.tabs{top:637px;left:0;width:1400px;height:86px;background:linear-gradient(#2e2e2e,#1e1e1e)}
.tabs span{position:absolute;top:0;height:86px;line-height:86px;color:#8a8a8a;font-weight:700;font-size:13px;text-align:center}
.tabs span.active{background:linear-gradient(#505050,#3c3c3c);color:#fff}

.trial h2{position:absolute;left:212px;top:762px;color:var(--accent);font-size:21px;font-weight:700}
.trial p{position:absolute;left:213px;top:798px;width:775px;color:var(--text);font-size:13px;line-height:23px}
.trial-btn{left:1021px;top:795px;width:168px;height:41px;background:var(--orange);color:#fff;font-size:14px;line-height:41px;text-align:center;border-radius:2px}
.rule{left:210px;top:861px;width:980px;height:1px;background:var(--rule)}

.section-title{left:0;top:893px;width:1412px;text-align:center;color:var(--accent);font-size:19px;font-weight:700}
.feature{top:963px;width:230px;text-align:center}
.badge{width:120px;height:120px;margin:0 auto;border-radius:50%;background:radial-gradient(circle at 50% 45%,var(--badge-dark) 0 50%,var(--badge-light) 52% 100%)}
.badge-shadow{width:90px;height:5px;margin:10px auto 0;border-radius:50%;background:#c4c4c4}
.feature h3{margin-top:14px;color:var(--accent);font-size:15px;font-weight:700}
.feature p{margin-top:8px;color:var(--text);font-size:11px;line-height:18px;height:72px}
.feature .more{display:inline-block;margin-top:14px;width:102px;height:28px;line-height:28px;background:var(--btn);color:#eee;font-size:11px;border-radius:2px}

.footer{top:1302px;left:0;width:1400px;height:130px;background:var(--footer)}
.footer ul{position:absolute;top:22px;list-style:none}
.footer li{color:var(--footer-text);font-size:11px;line-height:23px}
.news{left:686px;top:20px;color:#fff}
.news h4{font-size:13px;font-weight:400}
.news p{font-size:10px;color:var(--footer-text);margin-top:8px;white-space:nowrap}
.news .field{position:absolute;top:51px;left:0;width:212px;height:23px;background:#9a9a9a;color:#fff;font-size:9px;line-height:23px;padding-left:11px}
.news .submit{position:absolute;top:51px;left:220px;width:62px;height:23px;background:#383838;color:#fff;font-size:9px;line-height:23px;text-align:center}
.social{left:1033px;top:19px}
.social div{display:flex;align-items:center;gap:12px;height:31px;color:var(--footer-text);font-size:9px}
.social i{width:24px;height:24px;border-radius:50%;background:#707070;display:block}
.footer-bar{top:1432px;left:0;width:1400px;height:38px;background:var(--footer-bar);color:#ccc;font-size:9px;line-height:38px;text-align:center}
</style>
</head>
<body>
<div class="page">
  <header class="header abs">
    <div class="logo abs"><span class="logo-dot"></span><span class="logo-name">talvoro</span></div>
    <nav class="topnav">
      <a class="active" style="left:712px;width:86px">TOUR</a>
      <a style="left:840px;width:80px">FEATURES</a>
      <a style="left:974px;width:80px">PRICING</a>
      <a style="left:1100px;width:80px">SIGNUP</a>
    </nav>
  </header>

  <nav class="subnav abs">
    <a class="active" style="left:210px;width:92px">HOME</a>
    <a style="left:321px;width:60px">FAQ</a>
    <a style="left:412px;width:100px">DOWNLOAD</a>
    <a style="left:546px;width:150px">SUPPORT &amp; TRAINING</a>
    <a style="left:730px;width:100px">CUSTOMERS</a>
    <a style="left:863px;width:90px">ABOUT US</a>
    <a style="left:990px;width:60px">LOGIN</a>
    <a style="left:1088px;width:100px">CONTACT US</a>
  </nav>

  <section class="hero abs">
    <div class="hero-art abs" role="img" aria-label="Businessman seen from behind pressing a glowing project gear linked to user contact icons"></div>
    <div class="hero-copy abs">
      <h1>PROJECT<br>MANAGEMENT SOFTWARE</h1>
      <p>SIMPLE, EASY TO USE PROJECT MANAGEMENT SOFTWARE.</p>
    </div>
    <div class="hero-btn abs">VIEW MORE DETAILS</div>
  </section>

  <div class="tabs abs">
    <span class="active" style="left:210px;width:307px">PROJECT MANAGEMENT SOFTWARE</span>
    <span style="left:530px;width:184px">TIMESHEET SOFTWARE</span>
    <span style="left:748px;width:200px">RESOURCE MANAGEMENT</span>
    <span style="left:985px;width:170px">ISSUE MANAGEMENT</span>
  </div>

  <section class="trial">
    <h2>GET A FREE TRIAL</h2>
    <p>It has survived not only five centuries, but also the leap into electronic typesetting, remaining essentially unchanged. It was popularised in the 1960s with the release of Tesvander sheets containing</p>
    <div class="trial-btn abs">GET A FREE TRIAL</div>
  </section>
  <div class="rule abs"></div>

  <h2 class="section-title abs">PROJECT MANAGEMENT SOFTWARE</h2>

  <div class="feature abs" style="left:203px">
    <div class="badge" role="img" aria-label="Steel gear badge for project management"></div>
    <div class="badge-shadow"></div>
    <h3>PROJECT MANAGEMENT</h3>
    <p>Simple, easy to use project management software. Plan, Track and Improve your projects. Reduce costs and increase efficiency.</p>
    <span class="more">READ MORE</span>
  </div>

  <div class="feature abs" style="left:463px">
    <div class="badge" role="img" aria-label="Steel gear badge with a calendar for timesheets"></div>
    <div class="badge-shadow"></div>
    <h3>TIMESHEETS</h3>
    <p>Powerful hosted project time and status collection. Track expenses and time. Have an audit trail on your time billing. Timesheet software</p>
    <span class="more">READ MORE</span>
  </div>

  <div class="feature abs" style="left:720px">
    <div class="badge" role="img" aria-label="Steel gear badge with a light bulb for resource management"></div>
    <div class="badge-shadow"></div>
    <h3>RESOURCE MANAGEMENT</h3>
    <p>Plan, manage and control work for your whole organisation or a single project. Resource management</p>
    <span class="more">READ MORE</span>
  </div>

  <div class="feature abs" style="left:973px">
    <div class="badge" role="img" aria-label="Steel gear badge with small cogs for issues, risks and change"></div>
    <div class="badge-shadow"></div>
    <h3>ISSUES, RISKS AND CHANGE</h3>
    <p>Track and report on issues, risk and change. One click reports. issue management</p>
    <span class="more">READ MORE</span>
  </div>

  <footer class="footer abs">
    <ul style="left:215px"><li>HOME</li><li>FAQ</li><li>SUPPORT &amp; TRAINING</li><li>CONTACT US</li></ul>
    <ul style="left:395px"><li>TOUR</li><li>FEATURES</li><li>PRICING</li><li>SIGN UP</li></ul>
    <ul style="left:525px"><li>CAREERS</li><li>PRIVACY POLICY</li><li>TERMS OF SALE</li><li>SITEMAP</li></ul>
    <div class="news abs">
      <h4>NEWSLETTER SIGNUP</h4>
      <p>GET A UPDATE NEWS THROUGH YOUR MAIL</p>
      <div class="field">ENTER YOUR EMAIL ID :</div>
      <div class="submit">SUBMIT</div>
    </div>
    <div class="social abs">
      <div><i></i>CIRCLEPAGE</div>
      <div><i></i>LINKVERA</div>
      <div><i></i>CHIRPLINE</div>
    </div>
  </footer>
  <div class="footer-bar abs">COPYRIGHT © 2013. TALVORO. ALL RIGHTS RESERVED.</div>
</div>
</body>
</html>
```